Home Page Design for Motor Manufacturer

Hello,
please design the homepage for a manufacturer of industry motors. I am looking for a professional, clean and minimalistic design. Since this a rather conservative industry it should get a professional look but since it is a redesign there should be some modern that gives is the modern touch of innovation.
A competitor's homepage I like is:
https://www.valtrosen.com/en/
What I like about this website:
* clean, minimal, well structured design
* mega menu
For this project please find attached the wireframes (most buttons are in German but by context and Google translate you will easily figure it out; only unclear - "Messe" means "trade exhibition"). The paddings and margins are NOT exact. Also any color of backgrounds etc. chosen is not meant to represent a real color but rather to illustrate the object and maybe show there should be some background emphasis (color or image).
Wireframes:
https: //www.filquarry. com / t / pWmeTuZa8LkiBvQx
In both wireframes the only thing that is different is the Service section. I expect from the winner both designs for this service section: one with normal cart design and one with tabs as filters to search products (find image for product categories attached)
In the header use on the left the following text:
h1: "Your competent partner for industrial engines,
-transmission and drawing parts
with more than 5000 satisfied customers "
primary button: Our products
sec. button: Download catalog
and on the right side we feature one or more product images (like putting them in a nice display together).
I also think of a solid background color or subtle gradient for the hero section.
The winner should also design an open mega menu version.
Menu items in this order:
• Home page
• Gearboxes & Motors
• Engine components
• Drawing parts
• Machines & accessories
• About us
• Contact
Also create a language switch with globe symbol and DE for Germany and EN for English above the nav plus the telephone number with icon (user dummy number +49 (0) 987650432)
Output should be in Figma, Sketch or PSD.
Fonts + color to use:
header: Proza Libre, bold, # 0171A1
body: Open Sans, regular, black
Primary accent color: # 0171A1
Text black or dark gray
background: light gray, white or shade of blue
More image resources:
https://www.filquarry.com/t/RnaHwoqPEdLu5sjv
If there are any questions please do not hesitate to ask.
Target Market(s)
B2B - anyone with industrial machinery needing small motors (not car engines)
Industry/Entity Type
Manufacturing
Number of Pages Required
1 page
Requirements
Must have
- see above
Nice to have
- see above
Should not have
- see above

```html
<!DOCTYPE html>
<html lang="en">
<head>
<meta charset="utf-8">
<title>Kavrion – Industrial Motors &amp; Gearboxes</title>
<link href="https://fonts.googleapis.com/css2?family=Open+Sans:wght@400;600;700&family=Ubuntu:wght@400;500;700&display=swap" rel="stylesheet">
<style>
:root{
  --blue:#0171A1;
  --blue-dark:#015f88;
  --ink:#1c1c1c;
  --text:#555;
  --muted:#8a8a8a;
  --line:#e3e3e3;
  --gray-bg:#efefef;
  --white:#fff;
  --orange:#f5a623;
  --footer:#3b3b3b;
  --head:"Ubuntu",sans-serif;
  --body:"Open Sans",sans-serif;
}
*{box-sizing:border-box;margin:0;padding:0}
html,body{width:1200px;height:4773px;overflow:hidden}
body{position:relative;font-family:var(--body);color:var(--ink);background:var(--white)}
.abs{position:absolute}
a{color:inherit;text-decoration:none}
svg{display:block}

/* top bar */
.topbar{left:0;top:0;width:1200px;height:59px;background:var(--white)}
.brand{left:163px;top:12px;font-family:var(--head);font-weight:700;font-size:27px;color:var(--blue);letter-spacing:1px;display:flex;align-items:center;gap:8px}
.brand .mark{width:14px;height:14px;border-radius:50%;background:var(--blue)}
.search{left:317px;top:11px;width:387px;height:37px;display:flex;border:1px solid #d8d8d8;border-radius:19px;overflow:hidden}
.search .cat{width:87px;background:var(--blue);color:#fff;font-size:10px;display:flex;align-items:center;justify-content:center}
.search .field{flex:1;font-size:11px;color:var(--muted);padding:12px 16px}
.search .go{width:36px;border-left:1px solid #d8d8d8;display:flex;align-items:center;justify-content:center}
.call{left:762px;top:14px;display:flex;gap:8px;align-items:center}
.call small{display:block;font-size:8px;color:var(--muted)}
.call strong{display:block;font-size:12px;color:var(--blue);font-weight:700}
.lang{left:912px;top:20px;display:flex;gap:6px;align-items:center;font-size:11px;color:var(--text)}

/* nav */
.nav{left:0;top:59px;width:1200px;height:50px;background:var(--blue)}
.nav ul{list-style:none}
.nav li{position:absolute;top:17px;font-size:11px;font-weight:700;color:#fff;white-space:nowrap}
.nav .user{left:1013px;top:14px}

/* hero */
.hero{left:0;top:109px;width:1200px;height:524px;background:linear-gradient(180deg,#2c4a72 0%,#3d5f88 45%,#1b2940 100%)}
.hero-arrow{width:44px;height:44px;border-radius:50%;background:#1a1a1a;display:flex;align-items:center;justify-content:center;top:347px}
.hero-card{left:319px;top:231px;width:563px;height:262px;background:var(--white)}
.hero-card h1{position:absolute;left:25px;top:40px;font-family:var(--head);font-weight:700;font-size:28px;line-height:36px;color:var(--blue);width:350px}
.hero-card .lead{position:absolute;left:25px;top:125px;font-size:13px;line-height:21px;color:var(--ink);width:330px}
.btn{display:flex;align-items:center;justify-content:center;font-size:11px}
.btn-blue{background:var(--blue);color:#fff}
.btn-line{border:1px solid var(--blue);color:var(--ink);background:#fff}
.btn-dark{background:#111;color:#fff;font-weight:600}
.hero-card .b1{position:absolute;left:25px;top:193px;width:112px;height:28px}
.hero-card .b2{position:absolute;left:153px;top:193px;width:134px;height:28px}
.hero-card .side-img{position:absolute;left:422px;top:34px;width:92px;height:92px;border-radius:50%;background:radial-gradient(circle,#e7e7e7 20%,#9a9a9a 70%,#6b6b6b 100%)}
.hero-card .side-text{position:absolute;left:392px;top:150px;width:160px;font-size:11px;line-height:17px;color:var(--muted);text-align:center}
.hero-card .b3{position:absolute;left:424px;top:197px;width:90px;height:29px}

/* features */
.features{left:191px;top:559px;width:802px;height:260px;display:flex;gap:2px}
.feature{flex:1;background:#fff;box-shadow:0 2px 8px rgba(0,0,0,.1);position:relative;text-align:center}
.feature svg.ico{position:absolute;left:82px;top:30px}
.feature h3{position:absolute;left:0;right:0;top:79px;font-family:var(--head);font-weight:500;font-size:17px}
.feature p{position:absolute;left:18px;right:18px;top:122px;font-size:11px;line-height:15px;color:var(--muted)}
.feature .go{position:absolute;left:85px;top:204px;width:30px;height:30px;border-radius:50%;background:var(--blue);display:flex;align-items:center;justify-content:center}

/* section heads */
.band-gray{left:0;width:1200px;background:var(--gray-bg)}
.sec-title{font-family:var(--head);font-weight:500;font-size:27px;color:var(--ink)}
.rule{height:2px;background:#c9c9c9}
.rule i{display:block;width:72px;height:3px;background:var(--blue);margin-top:-1px}
.round{width:28px;height:28px;border-radius:50%;background:var(--blue);display:flex;align-items:center;justify-content:center}

/* products */
.cards{left:161px;width:878px;display:flex;gap:31px}
.card{width:196px;height:332px;background:#fff;position:relative;box-shadow:0 1px 5px rgba(0,0,0,.08);text-align:center}
.card .badge{position:absolute;left:0;top:0;background:var(--orange);color:#fff;font-size:8px;padding:3px 8px 3px 6px;display:flex;gap:3px;align-items:center;z-index:1}
.card .pic{position:absolute;left:30px;top:20px;width:136px;height:138px;border-radius:8px}
.pic-enc{background:radial-gradient(circle at 55% 45%,#3b8cc8 0%,#2a2a2a 45%,#bdbdbd 75%,#fff 100%)}
.pic-gear{background:radial-gradient(circle at 45% 45%,#4a4a4a 0%,#888 40%,#d6d6d6 70%,#fff 100%)}
.card h4{position:absolute;left:0;right:0;top:172px;font-size:12px;font-weight:700}
.card p{position:absolute;left:14px;right:14px;top:196px;font-size:10px;line-height:14px;color:var(--muted)}
.card .vd{position:absolute;left:0;right:0;top:258px;height:34px;background:var(--blue);color:#fff;font-size:11px;font-weight:700}
.card .qv{position:absolute;left:0;right:0;top:292px;height:40px;font-size:11px;font-weight:700}
.tabs{top:1486px;left:687px;display:flex;gap:10px}
.tab{height:32px;background:#e9e9e9;font-size:10px;color:var(--ink);display:flex;align-items:center;justify-content:center}
.tab.on{background:var(--blue);color:#fff}

/* measure up */
.mu{left:161px;width:870px;height:273px;background:#fff;box-shadow:0 1px 6px rgba(0,0,0,.08)}
.mu .pic{position:absolute;left:44px;top:42px;width:186px;height:186px;border-radius:50%;border:1px solid var(--line);background:radial-gradient(circle,#5a5a5a 0%,#a9a9a9 35%,#f2f2f2 65%,#fff 100%)}
.mu h3{position:absolute;left:265px;top:52px;font-family:var(--head);font-weight:500;font-size:19px}
.mu p{position:absolute;left:265px;top:84px;width:555px;font-size:10.5px;line-height:19.5px;color:var(--text)}
.mu .ft{position:absolute;left:600px;top:192px;width:101px;height:33px;font-weight:600}
.mu .vdt{position:absolute;left:713px;top:192px;width:102px;height:33px}

/* about */
.about-bar{left:161px;top:3182px;width:61px;height:253px;background:var(--blue)}
.about-text{left:250px;top:3184px;width:330px}
.about-text .strong{font-size:12.5px;line-height:22px;font-weight:600;color:var(--ink)}
.about-text p{font-size:11px;line-height:18px;color:var(--text);margin-top:14px}
.readmore{left:250px;top:3398px;width:111px;height:34px;background:#111;color:#fff;font-size:11px;font-weight:600}
.circle-big{left:677px;top:3126px;width:360px;height:360px;border-radius:50%;border:6px solid var(--blue);background:linear-gradient(160deg,#c9d6e6,#9fb0c6 50%,#2d3440)}
.circle-small{left:593px;top:3269px;width:222px;height:222px;border-radius:50%;border:5px solid var(--blue);background:radial-gradient(circle,#3e6fb0 0%,#1d1d1d 40%,#cfcfcf 70%,#fff 100%)}

/* downloads */
.dl-photo{left:0;top:3550px;width:600px;height:500px;background:linear-gradient(135deg,#7e8694,#c3c6cc 45%,#5c6270)}
.dl-side{left:600px;top:3550px;width:600px;height:500px;background:#f1f1f1}
.dl-text{left:663px;top:3620px;width:378px}
.dl-text p{font-size:10.5px;line-height:18px;color:var(--text);margin-top:18px}
.dl-btn{left:667px;top:3945px;width:135px;height:33px;border:1px solid var(--blue);background:#fff;font-size:11px;gap:4px}

/* contact */
.contact{left:0;top:4050px;width:1200px;height:271px;background:linear-gradient(180deg,#c9e4ea,#a5d2dc)}
.contact h2{position:absolute;left:0;right:0;top:58px;text-align:center}
.contact .in{position:absolute;top:121px;width:241px;height:33px;background:#fff;border:1px solid #d5d5d5;font-size:10px;color:var(--muted);padding:10px 17px}
.contact .sub{position:absolute;left:537px;top:187px;width:126px;height:35px;font-size:11px}

/* info row */
.info{top:4361px;display:flex;gap:12px}
.info h5{font-family:var(--head);font-weight:500;font-size:13px;margin-top:4px}
.info p{font-size:9.5px;line-height:15px;color:var(--muted);margin-top:5px}
.touch{left:917px;top:4372px;width:122px;height:32px;font-size:12px}
.hr{left:161px;top:4463px;width:878px;height:1px;background:var(--line)}

/* footer */
.fcol h6{font-family:var(--head);font-weight:500;font-size:12.5px;letter-spacing:.3px}
.fcol li{list-style:none;font-size:9.5px;color:var(--muted);line-height:24px}
.fcol ul{margin-top:12px}
.news-in{left:691px;top:4593px;width:244px;height:31px;border:1px solid #ddd;font-size:10px;color:var(--text);padding:9px 18px}
.news-btn{left:935px;top:4593px;width:104px;height:31px;font-size:11px}
.social{top:4638px;display:flex;gap:5px;left:692px}
.social span{width:28px;height:28px;border-radius:50%;background:var(--blue);display:block}
.bottom{left:0;top:4719px;width:1200px;height:54px;background:var(--footer);color:#ddd;font-size:9.5px}
.bottom .copy{position:absolute;left:161px;top:21px}
.bottom .links{position:absolute;right:161px;top:21px;display:flex;gap:20px}
</style>
</head>
<body>

<header class="abs topbar">
  <div class="abs brand"><span class="mark"></span>Kavrion</div>
  <div class="abs search">
    <div class="cat">Search Item</div>
    <div class="field">Search</div>
    <div class="go"><svg width="12" height="12" viewBox="0 0 12 12"><circle cx="5" cy="5" r="3.6" fill="none" stroke="#555" stroke-width="1.4"/><path d="M8 8l3 3" stroke="#555" stroke-width="1.4"/></svg></div>
  </div>
  <div class="abs call">
    <svg width="14" height="14" viewBox="0 0 24 24"><path fill="#0171A1" d="M6.6 10.8a15 15 0 006.6 6.6l2.2-2.2a1 1 0 011-.25 11.4 11.4 0 003.6.6 1 1 0 011 1V20a1 1 0 01-1 1A17 17 0 013 4a1 1 0 011-1h3.5a1 1 0 011 1c0 1.25.2 2.45.57 3.57a1 1 0 01-.25 1z"/></svg>
    <div><small>Call for Any Question</small><strong>+49 (0) 987650432</strong></div>
  </div>
  <div class="abs lang">
    <svg width="14" height="14" viewBox="0 0 24 24"><circle cx="12" cy="12" r="10" fill="#0171A1"/><path d="M2 12h20M12 2c3 3 3 17 0 20M12 2c-3 3-3 17 0 20" stroke="#fff" stroke-width="1.4" fill="none"/></svg>
    Select Language
    <svg width="8" height="8" viewBox="0 0 8 8"><path d="M1 2.5l3 3 3-3" stroke="#555" stroke-width="1.3" fill="none"/></svg>
  </div>
</header>

<nav class="abs nav">
  <ul>
    <li style="left:161px">Home</li>
    <li style="left:219px">Gearboxes &amp; Motors ⌄</li>
    <li style="left:365px">Engine Components ⌄</li>
    <li style="left:509px">Drawing Parts ⌄</li>
    <li style="left:624px">Machines &amp; Accessories ⌄</li>
    <li style="left:787px">About Us</li>
    <li style="left:863px">Contact</li>
  </ul>
  <svg class="abs user" width="20" height="22" viewBox="0 0 20 22"><circle cx="10" cy="7" r="5" fill="none" stroke="#fff" stroke-width="1.6"/><path d="M1.5 21c0-5 4-8 8.5-8s8.5 3 8.5 8z" fill="none" stroke="#fff" stroke-width="1.6"/></svg>
</nav>

<section class="abs hero" role="img" aria-label="Workshop photo of motors and gear parts on a production table"></section>
<div class="abs hero-arrow" style="left:8px"><svg width="10" height="12" viewBox="0 0 10 12"><path d="M7 1L2 6l5 5" stroke="#fff" stroke-width="2" fill="none"/></svg></div>
<div class="abs hero-arrow" style="left:1128px"><svg width="10" height="12" viewBox="0 0 10 12"><path d="M3 1l5 5-5 5" stroke="#fff" stroke-width="2" fill="none"/></svg></div>

<div class="abs hero-card">
  <h1>Your competent partner for industrial engines,</h1>
  <p class="lead">Transmission and drawing parts with more than 5000 satisfied customers</p>
  <a class="btn btn-blue b1">Our Products</a>
  <a class="btn btn-line b2">Download Catalog</a>
  <div class="side-img" role="img" aria-label="Precision gearbox product"></div>
  <p class="side-text">Lorem ipsum dolor sit amet, consectetur adipiscing elit.</p>
  <a class="btn btn-blue b3">View More</a>
</div>

<div class="abs features">
  <div class="feature"><svg class="ico" width="36" height="36" viewBox="0 0 36 36"><path d="M3 33V14l7-5v5l7-5v5l7-5v24M26 33V4h6v29" fill="none" stroke="#0171A1" stroke-width="2.2"/><path d="M7 20h4M14 20h4M21 20h3M7 26h4M14 26h4M21 26h3M1 33h34" stroke="#0171A1" stroke-width="2.2"/></svg><h3>Feature 01</h3><p>Lorem ipsum dolor sit amet, consectetur adipiscing elit. Donec faucibus consequat dui sit amet consequat.</p><div class="go"><svg width="8" height="10" viewBox="0 0 8 10"><path d="M2 1l4 4-4 4" stroke="#fff" stroke-width="1.8" fill="none"/></svg></div></div>
  <div class="feature"><svg class="ico" width="36" height="36" viewBox="0 0 36 36"><path d="M3 33V14l7-5v5l7-5v5l7-5v24M26 33V4h6v29" fill="none" stroke="#0171A1" stroke-width="2.2"/><path d="M7 20h4M14 20h4M21 20h3M7 26h4M14 26h4M21 26h3M1 33h34" stroke="#0171A1" stroke-width="2.2"/></svg><h3>Feature 02</h3><p>Lorem ipsum dolor sit amet, consectetur adipiscing elit. Donec faucibus consequat dui sit amet consequat.</p><div class="go"><svg width="8" height="10" viewBox="0 0 8 10"><path d="M2 1l4 4-4 4" stroke="#fff" stroke-width="1.8" fill="none"/></svg></div></div>
  <div class="feature"><svg class="ico" width="36" height="36" viewBox="0 0 36 36"><path d="M3 33V14l7-5v5l7-5v5l7-5v24M26 33V4h6v29" fill="none" stroke="#0171A1" stroke-width="2.2"/><path d="M7 20h4M14 20h4M21 20h3M7 26h4M14 26h4M21 26h3M1 33h34" stroke="#0171A1" stroke-width="2.2"/></svg><h3>Feature 03</h3><p>Lorem ipsum dolor sit amet, consectetur adipiscing elit. Donec faucibus consequat dui sit amet consequat.</p><div class="go"><svg width="8" height="10" viewBox="0 0 8 10"><path d="M2 1l4 4-4 4" stroke="#fff" stroke-width="1.8" fill="none"/></svg></div></div>
  <div class="feature"><svg class="ico" width="36" height="36" viewBox="0 0 36 36"><path d="M3 33V14l7-5v5l7-5v5l7-5v24M26 33V4h6v29" fill="none" stroke="#0171A1" stroke-width="2.2"/><path d="M7 20h4M14 20h4M21 20h3M7 26h4M14 26h4M21 26h3M1 33h34" stroke="#0171A1" stroke-width="2.2"/></svg><h3>Feature 04</h3><p>Lorem ipsum dolor sit amet, consectetur adipiscing elit. Donec faucibus consequat dui sit amet consequat.</p><div class="go"><svg width="8" height="10" viewBox="0 0 8 10"><path d="M2 1l4 4-4 4" stroke="#fff" stroke-width="1.8" fill="none"/></svg></div></div>
</div>

<!-- New products -->
<section class="abs band-gray" style="top:885px;height:526px"></section>
<h2 class="abs sec-title" style="left:161px;top:953px">New Products</h2>
<div class="abs round" style="left:970px;top:960px"><svg width="8" height="10" viewBox="0 0 8 10"><path d="M6 1L2 5l4 4" stroke="#fff" stroke-width="1.8" fill="none"/></svg></div>
<div class="abs round" style="left:1011px;top:960px"><svg width="8" height="10" viewBox="0 0 8 10"><path d="M2 1l4 4-4 4" stroke="#fff" stroke-width="1.8" fill="none"/></svg></div>
<div class="abs rule" style="left:161px;top:999px;width:878px"><i></i></div>

<div class="abs cards" style="top:1033px">
  <div class="card"><span class="badge">★ Featured</span><div class="pic pic-enc" role="img" aria-label="Motor with blue encoder"></div><h4>Product 01</h4><p>Lorem ipsum dolor sit amet, consectetur adipiscing elit. Proin eu felis felis.</p><div class="btn vd">VIEW DETAILS</div><div class="btn qv">QUICK VIEW</div></div>
  <div class="card"><div class="pic pic-gear" role="img" aria-label="Right-angle planetary gearbox"></div><h4>Product 02</h4><p>Lorem ipsum dolor sit amet, consectetur adipiscing elit. Proin eu felis felis.</p><div class="btn vd">VIEW DETAILS</div><div class="btn qv">QUICK VIEW</div></div>
  <div class="card"><span class="badge">★ Featured</span><div class="pic pic-enc" role="img" aria-label="Motor with blue encoder"></div><h4>Product 03</h4><p>Lorem ipsum dolor sit amet, consectetur adipiscing elit. Proin eu felis felis.</p><div class="btn vd">VIEW DETAILS</div><div class="btn qv">QUICK VIEW</div></div>
  <div class="card"><div class="pic pic-gear" role="img" aria-label="Right-angle planetary gearbox"></div><h4>Product 04</h4><p>Lorem ipsum dolor sit amet, consectetur adipiscing elit. Proin eu felis felis.</p><div class="btn vd">VIEW DETAILS</div><div class="btn qv">QUICK VIEW</div></div>
</div>

<!-- Products with tabs -->
<h2 class="abs sec-title" style="left:161px;top:1477px">Products</h2>
<div class="abs rule" style="left:161px;top:1525px;width:72px;background:var(--blue)"></div>
<div class="abs tabs">
  <span class="tab" style="width:63px">All</span>
  <span class="tab on" style="width:101px">Subcat 01</span>
  <span class="tab" style="width:72px">Subcat</span>
  <span class="tab" style="width:101px">Subcat 03</span>
</div>
<div class="abs round" style="left:115px;top:1711px"><svg width="8" height="10" viewBox="0 0 8 10"><path d="M6 1L2 5l4 4" stroke="#fff" stroke-width="1.8" fill="none"/></svg></div>
<div class="abs round" style="left:1059px;top:1711px"><svg width="8" height="10" viewBox="0 0 8 10"><path d="M2 1l4 4-4 4" stroke="#fff" stroke-width="1.8" fill="none"/></svg></div>

<div class="abs cards" style="top:1559px">
  <div class="card"><span class="badge">★ Featured</span><div class="pic pic-enc" role="img" aria-label="Motor with blue encoder"></div><h4>Product 01</h4><p>Lorem ipsum dolor sit amet, consectetur adipiscing elit. Proin eu felis felis.</p><div class="btn vd">VIEW DETAILS</div><div class="btn qv">QUICK VIEW</div></div>
  <div class="card"><div class="pic pic-gear" role="img" aria-label="Right-angle planetary gearbox"></div><h4>Product 02</h4><p>Lorem ipsum dolor sit amet, consectetur adipiscing elit. Proin eu felis felis.</p><div class="btn vd">VIEW DETAILS</div><div class="btn qv">QUICK VIEW</div></div>
  <div class="card"><span class="badge">★ Featured</span><div class="pic pic-enc" role="img" aria-label="Motor with blue encoder"></div><h4>Product 03</h4><p>Lorem ipsum dolor sit amet, consectetur adipiscing elit. Proin eu felis felis.</p><div class="btn vd">VIEW DETAILS</div><div class="btn qv">QUICK VIEW</div></div>
  <div class="card"><div class="pic pic-gear" role="img" aria-label="Right-angle planetary gearbox"></div><h4>Product 04</h4><p>Lorem ipsum dolor sit amet, consectetur adipiscing elit. Proin eu felis felis.</p><div class="btn vd">VIEW DETAILS</div><div class="btn qv">QUICK VIEW</div></div>
</div>

<!-- Measure up -->
<section class="abs band-gray" style="top:1937px;height:1100px"></section>
<h2 class="abs sec-title" style="left:0;width:1200px;text-align:center;top:2015px;font-size:26px">Measure Up</h2>

<article class="abs mu" style="top:2083px">
  <div class="pic" role="img" aria-label="Right-angle gearbox"></div>
  <h3>Title Here</h3>
  <p>Lorem ipsum dolor sit amet, consectetur adipiscing elit. Proin eu felis felis. Donec at pellentesque enim. Quisque vehicula nunc felis, ut porttitor ipsum convallis quis. Praesent vel facilisis ex. Mauris cursus sit amet augue ut porttitor. Integer pellentesque risus vitae pellentesque fringilla. In eu imperdiet enim. Integer dolor ligula, malesuada a dolor non, congue eleifend tortor.</p>
  <a class="btn btn-blue ft">Free Ticket</a><a class="btn btn-dark vdt">View Details</a>
</article>
<article class="abs mu" style="top:2374px">
  <div class="pic" role="img" aria-label="Right-angle gearbox"></div>
  <h3>Title Here</h3>
  <p>Lorem ipsum dolor sit amet, consectetur adipiscing elit. Proin eu felis felis. Donec at pellentesque enim. Quisque vehicula nunc felis, ut porttitor ipsum convallis quis. Praesent vel facilisis ex. Mauris cursus sit amet augue ut porttitor. Integer pellentesque risus vitae pellentesque fringilla. In eu imperdiet enim. Integer dolor ligula, malesuada a dolor non, congue eleifend tortor.</p>
  <a class="btn btn-blue ft">Free Ticket</a><a class="btn btn-dark vdt">View Details</a>
</article>
<article class="abs mu" style="top:2667px">
  <div class="pic" role="img" aria-label="Right-angle gearbox"></div>
  <h3>Title Here</h3>
  <p>Lorem ipsum dolor sit amet, consectetur adipiscing elit. Proin eu felis felis. Donec at pellentesque enim. Quisque vehicula nunc felis, ut porttitor ipsum convallis quis. Praesent vel facilisis ex. Mauris cursus sit amet augue ut porttitor. Integer pellentesque risus vitae pellentesque fringilla. In eu imperdiet enim. Integer dolor ligula, malesuada a dolor non, congue eleifend tortor.</p>
  <a class="btn btn-blue ft">Free Ticket</a><a class="btn btn-dark vdt">View Details</a>
</article>

<!-- About -->
<h2 class="abs sec-title" style="left:161px;top:3126px">About Us</h2>
<div class="abs about-bar"></div>
<div class="abs about-text">
  <div class="strong">Lorem ipsum dolor sit amet, consectetur adipiscing elit. Proin eu felis felis. Donec at pellentesque enim.</div>
  <p>Lorem Ipsum is simply dummy text of the printing and typesetting industry. Lorem Ipsum has been the industry's standard dummy text ever since the 1500s Lorem Ipsum is simply dummy text of the printing and typesetting industry.</p>
  <p>Lorem ipsum dolor sit amet, consectetur adipiscing elit. Proin eu felis felis.</p>
</div>
<a class="abs btn readmore">Read More</a>
<div class="abs circle-big" role="img" aria-label="Team photo at a trade exhibition booth"></div>
<div class="abs circle-small" role="img" aria-label="Geared DC motor"></div>

<!-- Downloads -->
<div class="abs dl-photo" role="img" aria-label="Gear and bearing components displayed in a glass cabinet"></div>
<section class="abs dl-side"></section>
<div class="abs dl-text">
  <h2 class="sec-title">Downloads</h2>
  <p>Lorem ipsum dolor sit amet, consectetur adipiscing elit. Proin eu felis felis. Donec at pellentesque enim. Quisque vehicula nunc felis, ut porttitor ipsum convallis quis. Praesent vel facilisis ex. Mauris cursus sit amet augue ut porttitor. Integer pellentesque risus vitae pellentesque fringilla. In eu imperdiet enim. Integer dolor ligula, malesuada a dolor non, congue eleifend tortor. Sed feugiat odio nec diam vulputate malesuada.</p>
  <p>Lorem ipsum dolor sit amet, consectetur adipiscing elit. Proin eu felis felis. Donec at pellentesque enim. Quisque vehicula nunc felis, ut porttitor ipsum convallis quis. Praesent vel facilisis ex. Mauris cursus sit amet augue ut porttitor. Integer pellentesque risus vitae pellentesque fringilla. In eu imperdiet enim. Integer dolor ligula, malesuada a dolor non, congue eleifend tortor. Sed feugiat odio nec diam vulputate malesuada.</p>
</div>
<a class="abs btn dl-btn">DOWNLOAD <svg width="10" height="10" viewBox="0 0 10 10"><path d="M5 0v6M2 3.5L5 6.5 8 3.5M1 9h8" stroke="#1c1c1c" stroke-width="1.6" fill="none"/></svg></a>

<!-- Contact -->
<section class="abs contact">
  <h2 class="sec-title">Contact Us</h2>
  <div class="in" style="left:356px">Phone</div>
  <div class="in" style="left:604px">Email Address</div>
  <a class="btn btn-blue sub">SUBMIT</a>
</section>

<div class="abs info" style="left:163px">
  <svg width="52" height="52" viewBox="0 0 52 52"><path d="M26 4a13 13 0 00-13 13c0 10 13 25 13 25s13-15 13-25A13 13 0 0026 4z" fill="none" stroke="#0171A1" stroke-width="2"/><circle cx="26" cy="17" r="5" fill="none" stroke="#0171A1" stroke-width="2"/><path d="M14 38l-10 9h44l-10-9" fill="none" stroke="#0171A1" stroke-width="2"/></svg>
  <div><h5>Address</h5><p>Lorem ipsum dolor sit<br>amet.</p></div>
</div>
<div class="abs info" style="left:402px">
  <svg width="52" height="52" viewBox="0 0 52 52"><path d="M4 16c0-6 10-8 22-8s22 2 22 8v4h-10v-5H14v5H4z" fill="none" stroke="#0171A1" stroke-width="2"/><path d="M10 24l4-5h24l4 5v20H10z" fill="none" stroke="#0171A1" stroke-width="2"/><text x="26" y="40" text-anchor="middle" font-family="Open Sans,sans-serif" font-size="11" font-weight="700" fill="#0171A1">24</text></svg>
  <div><h5>Contact Info</h5><p>+49 (0) 987650432<br>+49 (0) 987650432</p></div>
</div>
<div class="abs info" style="left:635px">
  <svg width="52" height="52" viewBox="0 0 52 52"><path d="M4 22l22-16 22 16v24H4z" fill="none" stroke="#0171A1" stroke-width="2"/><path d="M4 22l22 15 22-15M4 46l16-13M48 46L32 33" fill="none" stroke="#0171A1" stroke-width="2"/><rect x="14" y="14" width="24" height="14" fill="none" stroke="#0171A1" stroke-width="1.6"/></svg>
  <div><h5>Email Address</h5><p>info@example.com<br>info@example.com</p></div>
</div>
<a class="abs btn btn-blue touch">Get in Touch</a>
<div class="abs hr"></div>

<!-- Footer -->
<div class="abs fcol" style="left:161px;top:4503px"><h6>OUR SOLUTIONS</h6><ul><li>Lorem ipsum is dolor</li><li>Lorem ipsum is dolor</li><li>Lorem ipsum is dolor</li><li>Lorem ipsum is dolor</li><li>Lorem ipsum is dolor</li></ul></div>
<div class="abs fcol" style="left:389px;top:4503px"><h6>COMPANY</h6><ul><li>Home</li><li>Company News</li><li>Case Study</li><li>Awards</li><li>Contact Us</li></ul></div>
<div class="abs fcol" style="left:537px;top:4503px"><h6>&nbsp;</h6><ul><li>About Us</li><li>Products</li><li>FAQ's</li><li>Services</li><li>Our Team</li></ul></div>
<div class="abs fcol" style="left:691px;top:4503px"><h6>SUBSCRIBE OUR NEWSLETTER</h6><ul><li>Weekly Breaking News Analysis And Cutting Edge</li><li>Advices On Job Searching.</li></ul></div>
<div class="abs news-in">Email Address</div>
<a class="abs btn btn-blue news-btn">SUBSCRIBE</a>
<div class="abs social"><span></span><span></span><span></span><span></span></div>

<footer class="abs bottom">
  <div class="copy">Copyright © 2020. All Rights Reserved.</div>
  <div class="links"><span>Home</span><span>About</span><span>FAQs</span><span>Contact</span></div>
</footer>

</body>
</html>
```